Quillmere Healthcare Coming Soon Sign

I need a large (10 x5) road banner announcing the construction of our new medical practice at 3187 Marlowe Ferry Road in John's Island. The name of our practice is Quillmere Healthcare and we thought it would be fund to nick name it the "Quillmere Waystation". We'd like the tagline to read - "There's nothing healthy about driving an hour to see your doctor. So we're coming to you." Opening Late 2025 I have attached three logos as we have two other practices (Quillmere Urgent and Quillmere Aesthetics ) that should be present on the bottom of the sign but the main business is Quillmere Healthcare. For more information on our look/feel visit our website www.goplainwell-example.com (which should be somewhere on the banner as well)
Updates

The signage needs to say Coming Late Fall 2025!

Target Market(s)

Drive By traffic must be made aware that we are coming soon

Industry/Entity Type

Healthcare

Requirements
Nice to have
• Western Theme

```html
<!DOCTYPE html>
<html lang="en">
<head>
<meta charset="utf-8">
<title>Quillmere Healthcare – Coming Late Fall 2025</title>
<link rel="stylesheet" href="https://fonts.googleapis.com/css2?family=Montserrat:wght@700&family=Inter:wght@600;700&family=Ultra&display=swap">
<style>
  :root {
    --backdrop: #a4a4a4;
    --paper: #ffffff;
    --navy: #21325f;
    --sky: #67b4e4;
    --sky-text: #5aabdf;
    --red: #e8383d;
    --magenta: #e3197f;
    --charcoal: #2e3532;
    --rule: #cfcdbf;
    --grain: #f4f4ea;
  }
  * { margin: 0; padding: 0; box-sizing: border-box; }
  html, body { width: 1200px; height: 2207px; overflow: hidden; background: var(--backdrop); }
  .sign { position: relative; width: 1200px; height: 2207px; }
  .sign-frame { position: absolute; inset: 0; width: 1200px; height: 2207px; }
  .abs { position: absolute; left: 0; width: 1200px; text-align: center; }

  .brand-mark {
    position: absolute; left: 535px; top: 272px; width: 130px; height: 130px;
    border-radius: 50%; background: var(--sky);
  }
  .brand-name {
    top: 458px; font-family: "Montserrat", sans-serif; font-weight: 700;
    color: var(--navy); line-height: 1;
  }
  .brand-name .line-1 { display: block; font-size: 80px; letter-spacing: 10px; }
  .brand-name .line-2 { display: block; font-size: 56px; letter-spacing: 12px; margin-top: 20px; color: var(--sky); }

  .grain-panel {
    position: absolute; left: 134px; top: 713px; width: 932px; height: 359px;
    background: linear-gradient(90deg, var(--grain), #fbfbf5 50%, var(--grain));
  }
  .headline {
    top: 776px; font-family: "Ultra", "Rockwell", serif; font-weight: 400; color: var(--navy);
    font-size: 80px; line-height: 78px; letter-spacing: 1px;
  }
  .headline .accent { color: var(--red); }

  .tagline {
    top: 1150px; font-family: "Inter", sans-serif; font-weight: 600;
    color: var(--navy); font-size: 41px; line-height: 59px;
  }
  .tagline .payoff { display: block; color: var(--sky-text); font-weight: 700; font-size: 53px; line-height: 66px; }

  .rule { position: absolute; left: 229px; width: 742px; height: 2px; background: var(--rule); }
  .rule-top { top: 1392px; }
  .rule-bottom { top: 1667px; }
  .rule-divider { position: absolute; left: 599px; top: 1430px; width: 2px; height: 196px; background: var(--rule); }

  .practice { position: absolute; top: 1438px; width: 360px; text-align: center; font-family: "Montserrat", sans-serif; font-weight: 700; line-height: 1; }
  .practice-urgent { left: 213px; }
  .practice-aesthetics { left: 629px; }
  .practice .dot { display: block; width: 64px; height: 64px; margin: 0 auto 38px; border-radius: 50%; }
  .practice-urgent .dot { background: var(--red); }
  .practice-aesthetics .dot { background: var(--magenta); }
  .practice .line-1 { display: block; font-size: 38px; letter-spacing: 6px; color: var(--charcoal); }
  .practice .line-2 { display: block; font-size: 28px; letter-spacing: 10px; margin-top: 16px; }
  .practice-urgent .line-2 { color: var(--red); }
  .practice-aesthetics .line-2 { color: var(--magenta); font-size: 24px; letter-spacing: 7px; }

  .web-address {
    top: 1768px; font-family: "Inter", sans-serif; font-weight: 700;
    color: var(--paper); font-size: 34px; line-height: 44px;
  }
</style>
</head>
<body>
<main class="sign">
  <svg class="sign-frame" viewBox="0 0 1401 2576" preserveAspectRatio="none" aria-hidden="true">
    <rect x="123" y="133" width="1155" height="2307" fill="var(--paper)"/>
    <path d="M133,2430 L133,271 L310,271 A128,128 0 0 0 437,143 L966,143 A128,128 0 0 0 1093,271 L1268,271 L1268,2430 L700,2318 Z"
          fill="none" stroke="var(--navy)" stroke-width="20" stroke-linejoin="miter"/>
    <path d="M360,2022 L1040,2022 Q1046,2022 1047,2032 L1050,2055 Q1053,2068 1060,2082 L1065,2095 Q1068,2100 1068,2110 L1068,2150 Q1068,2158 1060,2158 L340,2158 Q333,2158 333,2150 L333,2110 Q333,2100 336,2095 L341,2082 Q348,2068 351,2055 L354,2032 Q355,2022 360,2022 Z"
          fill="var(--paper)" stroke="var(--navy)" stroke-width="10"/>
    <path d="M372,2036 L1030,2036 L1034,2058 Q1038,2072 1046,2088 L1050,2100 L1050,2140 L350,2140 L350,2100 L354,2088 Q362,2072 366,2058 Z"
          fill="var(--sky)"/>
    <g fill="var(--navy)">
      <polygon transform="translate(626,2258)" points="0,-20 5,-6 20,-6 8,3 12,18 0,9 -12,18 -8,3 -20,-6 -5,-6"/>
      <polygon transform="translate(700,2248)" points="0,-20 5,-6 20,-6 8,3 12,18 0,9 -12,18 -8,3 -20,-6 -5,-6"/>
      <polygon transform="translate(776,2258)" points="0,-20 5,-6 20,-6 8,3 12,18 0,9 -12,18 -8,3 -20,-6 -5,-6"/>
    </g>
  </svg>

  <div class="brand-mark" aria-hidden="true"></div>
  <h1 class="abs brand-name"><span class="line-1">QUILLMERE</span><span class="line-2">HEALTHCARE</span></h1>

  <div class="grain-panel" role="img" aria-label="Pale wood grain texture behind the opening date"></div>
  <h2 class="abs headline"><span class="accent">COMING</span><br>LATE<br>FALL 2025!</h2>

  <p class="abs tagline">There's nothing healthy about<br>driving an hour to see your doctor.<span class="payoff">So we're coming to you.</span></p>

  <div class="rule rule-top"></div>
  <div class="rule-divider"></div>
  <div class="rule rule-bottom"></div>

  <div class="practice practice-urgent"><span class="dot"></span><span class="line-1">QUILLMERE</span><span class="line-2">URGENT</span></div>
  <div class="practice practice-aesthetics"><span class="dot"></span><span class="line-1">QUILLMERE</span><span class="line-2">AESTHETICS</span></div>

  <p class="abs web-address">www.goplainwell-example.com</p>
</main>
</body>
</html>
```